Influencer agency website

K-Brightline, Influencer Marketing Agency. A creative space where influencers and brands meet. We represent ideas and collaborations which bring marketing success to companies and brands.
Influencer types: Nano, Micro, Macro
Brand Types: Fashion, Beauty, Luxury Goods, Gaming, Sports, Home & Living, Travel, Lifestyle, Automotive

```html
<!DOCTYPE html>
<html lang="en">
<head>
<meta charset="utf-8">
<title>K-Brightline – Influencer Marketing Agency</title>
<link href="https://fonts.googleapis.com/css2?family=Roboto:wght@400;500;700;900&display=swap" rel="stylesheet">
<style>
:root{
  --black:#000;
  --white:#fff;
  --tan:#b89a82;
  --tan-light:#c7a993;
  --tan-dark:#a4876f;
  --mocha:#7a6560;
  --smoke:#5a5050;
  --hero-a:#d9d5d2;
  --hero-b:#b9b1ac;
  --ghost:rgba(255,255,255,.05);
}
*{margin:0;padding:0;box-sizing:border-box}
html,body{width:1200px;height:3315px;overflow:hidden;background:var(--black);font-family:'Roboto',sans-serif;color:var(--white)}
.page{position:relative;width:1200px;height:3315px}
.abs{position:absolute}
.header{left:0;top:0;width:1200px;height:82px;background:var(--black);z-index:3}
.brand-box{left:70px;top:0;width:181px;height:147px;background:var(--black);border-bottom:2px solid #222;z-index:4;display:flex;align-items:center;justify-content:center;gap:8px}
.brand-box .dot{width:10px;height:10px;background:var(--tan)}
.brand-box span{font-size:19px;font-weight:500;color:var(--tan)}
.nav a{position:absolute;top:36px;font-size:15px;color:var(--tan-light);text-decoration:none;letter-spacing:.2px}
.btn-quote{left:926px;top:24px;width:162px;height:42px;background:var(--tan);color:var(--white);font-weight:700;font-size:15px;display:flex;align-items:center;justify-content:center}
.hero{left:0;top:82px;width:1200px;height:599px;background:linear-gradient(90deg,var(--hero-a),var(--hero-b))}
.ph{display:block}
.hero-title{left:111px;top:268px;color:#111}
.hero-title .small{font-size:41px;font-weight:700;line-height:1}
.hero-title .big{font-size:74px;font-weight:900;line-height:1.05;letter-spacing:-.5px}
.hero-text{left:111px;top:402px;width:420px;color:#333;font-size:15.5px;line-height:21px}
.btn{display:flex;align-items:center;justify-content:center;font-weight:700;font-size:15px;color:var(--white)}
.btn-dark{left:111px;top:481px;width:132px;height:42px;background:#5a4f4c}
.btn-tan{background:var(--tan);width:132px;height:42px}
.arrow{width:33px;height:33px;border-radius:50%}
.intro{left:200px;top:773px;width:800px;text-align:center;font-size:16px;line-height:24px}
.ghost{color:var(--ghost);font-weight:900;white-space:nowrap;line-height:1}
.sec-title{width:1200px;left:0;text-align:center;color:var(--tan);font-weight:700;font-size:44px}
.sec-sub{left:180px;width:840px;text-align:center;font-size:16px;line-height:24px}
.card{width:232px;height:68px;border:1.5px solid var(--tan);border-radius:3px;display:flex;align-items:center;padding-left:22px;gap:18px;font-size:17px;font-weight:500}
.card .ic{width:44px;height:40px;border-radius:6px}
.lifestyle{left:0;top:1340px;width:1200px;height:523px;background:linear-gradient(90deg,var(--mocha),var(--smoke) 60%,#6e5a54)}
.feat-title{left:108px;font-size:42px;font-weight:700}
.feat-text{left:111px;width:435px;font-size:15.5px;line-height:24px}
.frame{border:3px solid var(--tan);width:322px;height:342px}
.inf-card{width:230px;height:215px;text-align:center;padding:28px 20px 0}
.inf-card h3{font-size:24px;font-weight:500;margin-bottom:10px}
.inf-card p{font-size:10.5px;line-height:17px}
.inf-card a{display:inline-block;margin-top:8px;font-size:15px;font-weight:500;color:var(--white);text-decoration:underline}
.footer{left:0;top:3052px;width:1200px;height:263px;background:linear-gradient(180deg,#c4a48c,#c8aa94)}
.email{left:330px;top:3093px;width:350px;height:46px;border:1.5px solid var(--white);font-size:12px;display:flex;align-items:center;padding-left:26px}
.subscribe{left:680px;top:3093px;width:191px;height:46px;background:var(--white);color:var(--tan-dark);font-weight:700;font-size:16px;display:flex;align-items:center;justify-content:center}
.fnav span{position:absolute;top:3176px;font-size:15px}
.rule{height:1px;background:var(--white);top:3238px}
.social{top:3228px;width:20px;height:20px;border-radius:50%;background:var(--white)}
.copy{left:0;width:1200px;top:3280px;text-align:center;font-size:11px}
.chat{left:1076px;top:3026px;width:54px;height:54px;border-radius:50%;background:var(--white)}
</style>
</head>
<body>
<div class="page">

  <header class="abs header">
    <nav class="nav">
      <a style="left:268px">HOME</a>
      <a style="left:361px">ABOUT US</a>
      <a style="left:485px">INFLUENCER</a>
      <a style="left:622px">BRAND TYPES</a>
      <a style="left:773px">CONTACT US</a>
    </nav>
    <div class="abs btn-quote">GET A FREE QUOTE</div>
  </header>
  <div class="abs brand-box"><i class="dot"></i><span>K-Brightline</span></div>

  <section class="abs hero"></section>
  <svg class="abs ph" style="left:620px;top:82px" width="580" height="599" role="img" aria-label="Portrait of a woman with long wavy red hair">
    <defs><linearGradient id="hair" x1="0" x2="1"><stop offset="0" stop-color="#c8c1bc" stop-opacity="0"/><stop offset=".35" stop-color="#b5714a"/><stop offset=".7" stop-color="#d9a58a"/><stop offset="1" stop-color="#c7bfb9"/></linearGradient></defs>
    <rect width="580" height="599" fill="url(#hair)" opacity=".85"/>
  </svg>
  <svg class="abs ph" style="left:510px;top:530px" width="290" height="192" role="img" aria-label="Group of skincare bottles and jars">
    <rect width="290" height="192" rx="14" fill="#c9d4cf"/>
  </svg>
  <div class="abs hero-title"><div class="small">Welcome To</div><div class="big">K-Brightline</div></div>
  <p class="abs hero-text">The standard chunk of Lorem Ipsum used since the 1500s is reproduced below for those interested. Sections 1.10.32 and 1.10.33 from "de Finibus Bonorum</p>
  <div class="abs btn btn-dark">GET STARTED</div>
  <svg class="abs arrow" style="left:37px;top:366px" width="33" height="33"><circle cx="16.5" cy="16.5" r="16.5" fill="#5a4f4c"/><path d="M19 10l-6 6.5 6 6.5" stroke="#fff" stroke-width="2.5" fill="none"/></svg>
  <svg class="abs arrow" style="left:1131px;top:366px" width="33" height="33"><circle cx="16.5" cy="16.5" r="16.5" fill="#5a4f4c"/><path d="M14 10l6 6.5-6 6.5" stroke="#fff" stroke-width="2.5" fill="none"/></svg>

  <p class="abs intro">The standard chunk of Lorem Ipsum used since the 1500s is reproduced below for those interested. Sections 1.10.32 and 1.10.33 from "de Finibus Bonorum et Malorum" by Veranius are also reproduced in their exact original form, accompanied by English versions from the 1914 translation by H. Ashcombe.</p>

  <div class="abs ghost" style="left:30px;top:870px;font-size:160px">BRAND TYPES</div>
  <h2 class="abs sec-title" style="top:935px">BRAND TYPES</h2>
  <p class="abs sec-sub" style="top:1001px">The standard chunk of Lorem Ipsum used since the 1500s is reproduced below for those interested. Sections 1.10.32 and 1.10.33 from "de Finibus Bonorum et Malorum" by Veranius are also</p>

  <div class="abs card" style="left:111px;top:1080px"><svg class="ic" role="img" aria-label="Fashion icon"><rect width="44" height="40" rx="6" fill="#e6c98a"/></svg>Fashion</div>
  <div class="abs card" style="left:359px;top:1080px"><svg class="ic" role="img" aria-label="Beauty icon"><rect width="44" height="40" rx="6" fill="#4a7fc2"/></svg>Beauty</div>
  <div class="abs card" style="left:608px;top:1080px"><svg class="ic" role="img" aria-label="Luxury goods icon"><rect width="44" height="40" rx="6" fill="#e8b64a"/></svg>Luxury Goods</div>
  <div class="abs card" style="left:857px;top:1080px"><svg class="ic" role="img" aria-label="Gaming icon"><rect width="44" height="40" rx="6" fill="#3f4f7a"/></svg>Gaming</div>
  <div class="abs card" style="left:111px;top:1173px"><svg class="ic" role="img" aria-label="Sports icon"><rect width="44" height="40" rx="6" fill="#d5703a"/></svg>Sports</div>
  <div class="abs card" style="left:359px;top:1173px"><svg class="ic" role="img" aria-label="Home and living icon"><rect width="44" height="40" rx="6" fill="#e9a84a"/></svg>Home &amp; Living</div>
  <div class="abs card" style="left:608px;top:1173px"><svg class="ic" role="img" aria-label="Travel icon"><rect width="44" height="40" rx="6" fill="#d9483a"/></svg>Travel</div>
  <div class="abs card" style="left:857px;top:1173px"><svg class="ic" role="img" aria-label="Automotive icon"><rect width="44" height="40" rx="6" fill="#3f7fc8"/></svg>Automotive</div>

  <section class="abs lifestyle"></section>
  <div class="abs ghost" style="left:20px;top:1345px;font-size:140px">LIFESTYLE</div>
  <h2 class="abs feat-title" style="top:1438px">LIFESTYLE</h2>
  <p class="abs feat-text" style="top:1500px">There are many variations of passages of Lorem Ipsum available, but the majority have suffered alteration in some form, by injected humour, or randomised words which don't look even slightly believable. If you are going to use a passage of Lorem Ipsum, you need to be sure there isn't anything embarrassing hidden in the middle of text. All the Lorem Ipsum generators on the Internet tend to repeat predefined chunks as necessary,</p>
  <div class="abs btn btn-tan" style="left:111px;top:1713px">GET STARTED</div>
  <div class="abs frame" style="left:766px;top:1448px"></div>
  <svg class="abs ph" style="left:833px;top:1518px" width="255" height="271" role="img" aria-label="Woman in a yellow dress sitting by a resort pool with palm trees"><defs><linearGradient id="resort" x1="0" y1="0" x2="0" y2="1"><stop offset="0" stop-color="#e9d9bf"/><stop offset=".5" stop-color="#b9a37a"/><stop offset="1" stop-color="#c88a5a"/></linearGradient></defs><rect width="255" height="271" fill="url(#resort)"/></svg>
  <svg class="abs ph" style="left:600px;top:1378px" width="322" height="342" role="img" aria-label="Woman in a sun hat lounging beside a blue swimming pool"><defs><linearGradient id="pool" x1="0" y1="0" x2="1" y2="1"><stop offset="0" stop-color="#4fb0d8"/><stop offset=".6" stop-color="#8fd0e6"/><stop offset="1" stop-color="#d8cfc2"/></linearGradient></defs><rect width="322" height="342" fill="url(#pool)"/></svg>

  <div class="abs ghost" style="left:0;top:1920px;font-size:150px">OUR INFLUENCER</div>
  <h2 class="abs sec-title" style="top:1967px">OUR INFLUENCER</h2>
  <p class="abs sec-sub" style="top:2033px">The standard chunk of Lorem Ipsum used since the 1500s is reproduced below for those interested. Sections 1.10.32 and 1.10.33 from "de Finibus Bonorum et Malorum" by Veranius are also</p>

  <div class="abs inf-card" style="left:206px;top:2127px;background:linear-gradient(180deg,#a88a74,#c2a28a)"><h3>Nano</h3><p>The standard chunk of Lorem Ipsum used since the 1500s is reproduced below for those interested. Sections 1.10.32 and 1.10.33 from "de Finibus Bonorum et Malorum"</p><a>Get Started</a></div>
  <div class="abs inf-card" style="left:485px;top:2127px;background:linear-gradient(180deg,#5e5452,#a88b76)"><h3>Micro</h3><p>The standard chunk of Lorem Ipsum used since the 1500s is reproduced below for those interested. Sections 1.10.32 and 1.10.33 from "de Finibus Bonorum et Malorum"</p><a>Get Started</a></div>
  <div class="abs inf-card" style="left:764px;top:2127px;background:linear-gradient(180deg,#a88a74,#c2a28a)"><h3>Macro</h3><p>The standard chunk of Lorem Ipsum used since the 1500s is reproduced below for those interested. Sections 1.10.32 and 1.10.33 from "de Finibus Bonorum et Malorum"</p><a>Get Started</a></div>

  <h2 class="abs feat-title" style="top:2540px">FASHION &amp; BEAUTY</h2>
  <p class="abs feat-text" style="top:2602px">There are many variations of passages of Lorem Ipsum available, but the majority have suffered alteration in some form, by injected humour, or randomised words which don't look even slightly believable. If you are going to use a passage of Lorem Ipsum, you need to be sure there isn't anything embarrassing hidden in the middle of text. All the Lorem Ipsum generators on the Internet tend to repeat predefined chunks as necessary,</p>
  <div class="abs btn btn-tan" style="left:111px;top:2815px">GET STARTED</div>
  <div class="abs frame" style="left:766px;top:2550px"></div>
  <svg class="abs ph" style="left:833px;top:2620px" width="255" height="272" role="img" aria-label="Smiling woman with curly hair holding a skincare bottle"><defs><linearGradient id="curly" x1="0" y1="0" x2="0" y2="1"><stop offset="0" stop-color="#e8dac6"/><stop offset="1" stop-color="#c99a78"/></linearGradient></defs><rect width="255" height="272" fill="url(#curly)"/></svg>
  <svg class="abs ph" style="left:600px;top:2480px" width="322" height="343" role="img" aria-label="Woman in a white bathrobe holding a lotion bottle"><defs><linearGradient id="robe" x1="0" y1="0" x2="0" y2="1"><stop offset="0" stop-color="#c9c9c9"/><stop offset="1" stop-color="#e6e4e2"/></linearGradient></defs><rect width="322" height="343" fill="url(#robe)"/></svg>
  <svg class="abs arrow" style="left:37px;top:2748px" width="33" height="33"><circle cx="16.5" cy="16.5" r="16.5" fill="#3a3331"/><path d="M19 10l-6 6.5 6 6.5" stroke="#000" stroke-width="2.5" fill="none"/></svg>
  <svg class="abs arrow" style="left:1131px;top:2748px" width="33" height="33"><circle cx="16.5" cy="16.5" r="16.5" fill="var(--tan)"/><path d="M14 10l6 6.5-6 6.5" stroke="#000" stroke-width="2.5" fill="none"/></svg>
  <div class="abs ghost" style="left:495px;top:2910px;font-size:150px;color:rgba(255,255,255,.06)">FASHION</div>

  <footer class="abs footer"></footer>
  <svg class="abs chat" width="54" height="54"><circle cx="27" cy="27" r="27" fill="#fff"/><circle cx="27" cy="27" r="12" fill="none" stroke="#7a6560" stroke-width="2.5"/><circle cx="22" cy="27" r="1.8" fill="#7a6560"/><circle cx="27" cy="27" r="1.8" fill="#7a6560"/><circle cx="32" cy="27" r="1.8" fill="#7a6560"/></svg>
  <div class="abs email">Your Email Address</div>
  <div class="abs subscribe">SUBSCRIBE NOW</div>
  <div class="fnav">
    <span style="left:190px">HOME</span><span style="left:284px">|</span>
    <span style="left:338px">ABOUT US</span><span style="left:462px">|</span>
    <span style="left:515px">INFLUENCER</span><span style="left:653px">|</span>
    <span style="left:706px">BRAND TYPES</span><span style="left:858px">|</span>
    <span style="left:912px">CONTACT US</span>
  </div>
  <div class="abs rule" style="left:111px;width:352px"></div>
  <div class="abs rule" style="left:737px;width:351px"></div>
  <div class="abs social" style="left:525px"></div>
  <div class="abs social" style="left:567px"></div>
  <div class="abs social" style="left:608px"></div>
  <div class="abs social" style="left:650px"></div>
  <p class="abs copy">© Copyright 2023 K-Brightline | All Rights Reserved.</p>

</div>
</body>
</html>
```